Corvane Supplies Business Card

Professional business card that stand out to our potential customers. Front and back with clean modern design

Industry/Entity Type

Oil and gas

Contact Information for Business Card

Name, address, website , office phone and cell number

Requirements
Must have
• Editable files for each employee

```html
<!DOCTYPE html>
<html lang="en">
<head>
<meta charset="utf-8">
<title>Corvane Supplies Business Card</title>
<link href="https://fonts.googleapis.com/css2?family=Montserrat:wght@400;500;700&display=swap" rel="stylesheet">
<style>
  :root {
    --backdrop: #3a3a3a;
    --card: #f2f2f2;
    --red: #e01e24;
    --blue: #10a0c6;
    --ink: #222222;
  }
  * { margin: 0; padding: 0; box-sizing: border-box; }
  html, body { width: 1200px; height: 1059px; overflow: hidden; }
  body {
    background: var(--backdrop);
    font-family: "Montserrat", sans-serif;
    color: var(--ink);
    position: relative;
  }
  .card {
    position: absolute;
    background: var(--card);
    border-radius: 24px;
  }
  .card-front { left: 256px; top: 100px; width: 688px; height: 393px; }
  .card-back { left: 253px; top: 536px; width: 694px; height: 396px; }

  .identity {
    position: absolute;
    right: 375px;
    top: 158px;
    text-align: right;
  }
  .person-name {
    font-weight: 700;
    font-size: 31px;
    letter-spacing: 0.5px;
    line-height: 1;
    white-space: nowrap;
  }
  .first-name { color: var(--red); }
  .last-name { color: var(--blue); }
  .job-title {
    font-weight: 500;
    font-size: 17px;
    margin-top: 12px;
  }
  .divider {
    position: absolute;
    left: 341px;
    top: 147px;
    width: 2px;
    height: 98px;
    background: var(--red);
  }
  .contact-list {
    position: absolute;
    left: 374px;
    top: 141px;
    list-style: none;
  }
  .contact-item {
    display: flex;
    align-items: center;
    height: 27.3px;
    font-size: 16.5px;
    font-weight: 500;
    white-space: nowrap;
  }
  .contact-icon {
    width: 16px;
    height: 16px;
    margin-right: 10px;
    flex: none;
  }
  .address {
    position: absolute;
    left: 0;
    right: 0;
    top: 341px;
    text-align: center;
    font-size: 16.5px;
    font-weight: 500;
  }

  .brand {
    position: absolute;
    left: 0;
    right: 0;
    top: 174px;
    display: flex;
    justify-content: center;
    align-items: center;
    gap: 16px;
  }
  .brand-square {
    width: 34px;
    height: 34px;
    background: var(--blue);
  }
  .brand-name {
    font-weight: 700;
    font-size: 40px;
    color: var(--red);
    letter-spacing: 0.5px;
    line-height: 1;
  }
</style>
</head>
<body>
  <section class="card card-front">
    <div class="identity">
      <h1 class="person-name"><span class="first-name">DALE</span> <span class="last-name">WHITFORD</span></h1>
      <p class="job-title">Managing Director</p>
    </div>
    <div class="divider"></div>
    <ul class="contact-list">
      <li class="contact-item">
        <svg class="contact-icon" viewBox="0 0 16 16" aria-hidden="true"><path fill="#e01e24" d="M1 6c0-2 3-3 7-3s7 1 7 3v1h-3V5.5H4V7H1zM3 8h10l1 5H2zM6 9.5h4v2H6z"/></svg>
        (555)014-0388
      </li>
      <li class="contact-item">
        <svg class="contact-icon" viewBox="0 0 16 16" aria-hidden="true"><rect x="4" y="1" width="8" height="14" rx="1.5" fill="none" stroke="#e01e24" stroke-width="1.6"/><circle cx="8" cy="12.5" r="0.9" fill="#e01e24"/></svg>
        555 201 774
      </li>
      <li class="contact-item">
        <svg class="contact-icon" viewBox="0 0 16 16" aria-hidden="true"><rect x="1" y="3.5" width="14" height="9" fill="#e01e24"/><path d="M1 3.5l7 5 7-5M1 12.5l5-4M15 12.5l-5-4" stroke="#f2f2f2" stroke-width="1.2" fill="none"/></svg>
        sales@corvanesupplies.com
      </li>
      <li class="contact-item">
        <svg class="contact-icon" viewBox="0 0 16 16" aria-hidden="true"><circle cx="8" cy="8" r="6.5" fill="#e01e24"/><path d="M5 4c1 1 2 1 2 2.5S5 8 5.5 10s1.5 2 1.5 3M10 3.5c0 1.5 1.5 1.5 2 3s-1.5 2-1 4" stroke="#f2f2f2" stroke-width="1.1" fill="none"/></svg>
        www.corvanesupplies.com
      </li>
    </ul>
    <p class="address">412 N.Larkmoor Suite 6 Midland, Tx 79701</p>
  </section>

  <section class="card card-back">
    <div class="brand">
      <span class="brand-square"></span>
      <span class="brand-name">CORVANE SUPPLIES</span>
    </div>
  </section>
</body>
</html>
```